Commercial facility maintenance

I need a card design that helps my salesmen make contact with new clients, our product is facility maintenance and heavy industrial maintenance

```html
<!DOCTYPE html>
<html lang="en">
<head>
<meta charset="utf-8">
<title>Business Card – Harlow Millworks LLC.</title>
<link href="https://fonts.googleapis.com/css2?family=Open+Sans:wght@400;600&family=Merriweather:wght@700&display=swap" rel="stylesheet">
<style>
  :root {
    --backdrop: #141415;
    --card-front: #ffffff;
    --card-back: #1f1f20;
    --pattern-light: #2c2c2e;
    --pattern-dark: #19191a;
    --accent-red: #9e1b24;
    --ink-dark: #2f3337;
    --ink-grey: #555a5f;
    --rule: #6c6f73;
    --back-text: #e6e6e6;
  }
  * { margin: 0; padding: 0; box-sizing: border-box; }
  html, body {
    width: 1200px;
    height: 900px;
    overflow: hidden;
    background: var(--backdrop);
  }
  .canvas {
    width: 1200px;
    height: 900px;
    display: flex;
    flex-direction: column;
    align-items: center;
    justify-content: center;
    gap: 40px;
  }
  .card {
    position: relative;
    width: 700px;
    height: 400px;
    flex: none;
    font-family: "Open Sans", Arial, sans-serif;
  }

  /* Front */
  .card-front {
    background: var(--card-front);
    color: var(--ink-grey);
  }
  .person {
    position: absolute;
    left: 45px;
    top: 48px;
  }
  .person-name {
    font-family: "Merriweather", Georgia, serif;
    font-weight: 700;
    font-size: 25px;
    letter-spacing: 0.3px;
    text-transform: uppercase;
    color: var(--accent-red);
    line-height: 1.15;
  }
  .person-title {
    font-size: 18px;
    line-height: 1.4;
    color: var(--ink-grey);
  }
  .brand {
    position: absolute;
    right: 45px;
    top: 42px;
    display: flex;
    align-items: center;
    gap: 14px;
  }
  .brand-dot {
    width: 56px;
    height: 56px;
    border-radius: 50%;
    background: var(--ink-dark);
    flex: none;
  }
  .brand-name {
    font-weight: 600;
    font-size: 21px;
    letter-spacing: 1px;
    text-transform: uppercase;
    color: var(--ink-dark);
    white-space: nowrap;
  }
  .divider {
    position: absolute;
    left: 45px;
    right: 45px;
    top: 122px;
    height: 1.5px;
    background: var(--rule);
  }
  .contact-list {
    position: absolute;
    left: 45px;
    top: 136px;
    list-style: none;
  }
  .contact-item {
    display: flex;
    align-items: center;
    gap: 9px;
    font-size: 18px;
    line-height: 30px;
    color: var(--ink-grey);
  }
  .contact-icon {
    width: 15px;
    height: 15px;
    flex: none;
  }
  .address {
    position: absolute;
    right: 45px;
    bottom: 42px;
    font-style: normal;
    font-size: 18px;
    line-height: 28px;
    color: var(--ink-grey);
  }

  /* Back */
  .card-back {
    background: var(--card-back);
    overflow: hidden;
  }
  .back-pattern {
    position: absolute;
    inset: 0;
    background: linear-gradient(135deg, var(--pattern-light), var(--pattern-dark));
  }
  .back-brand {
    position: absolute;
    right: 40px;
    bottom: 34px;
    display: flex;
    align-items: center;
    gap: 10px;
  }
  .back-brand-dot {
    width: 30px;
    height: 30px;
    border-radius: 50%;
    background: var(--accent-red);
    flex: none;
  }
  .back-brand-name {
    font-weight: 600;
    font-size: 15px;
    letter-spacing: 1px;
    text-transform: uppercase;
    color: var(--back-text);
    white-space: nowrap;
  }
</style>
</head>
<body>
<main class="canvas">
  <section class="card card-front">
    <div class="person">
      <h1 class="person-name">Jonathan Smith</h1>
      <p class="person-title">Managing Director</p>
    </div>

    <div class="brand">
      <span class="brand-dot" aria-hidden="true"></span>
      <p class="brand-name">Harlow Millworks LLC.</p>
    </div>

    <div class="divider"></div>

    <ul class="contact-list">
      <li class="contact-item">
        <svg class="contact-icon" viewBox="0 0 20 20" aria-hidden="true">
          <circle cx="10" cy="10" r="10" fill="#9e1b24"/>
          <path d="M6.5 5.5c.6-.5 1.2-.4 1.5.1l1 1.6c.3.5.1 1-.3 1.3l-.6.4c.5 1.1 1.4 2 2.5 2.6l.4-.6c.3-.4.9-.6 1.3-.3l1.6 1c.5.3.6.9.1 1.5-.7.8-1.6 1.1-2.6.7-2.4-1-4.3-2.9-5.2-5.3-.4-1 0-2 .3-3z" fill="#fff"/>
        </svg>
        <span>044-123 456 789</span>
      </li>
      <li class="contact-item">
        <svg class="contact-icon" viewBox="0 0 20 20" aria-hidden="true">
          <circle cx="10" cy="10" r="10" fill="#9e1b24"/>
          <rect x="5" y="6.5" width="10" height="7" fill="none" stroke="#fff" stroke-width="1.4"/>
          <path d="M5 6.5l5 4 5-4" fill="none" stroke="#fff" stroke-width="1.4"/>
        </svg>
        <span>info@webname.com</span>
      </li>
      <li class="contact-item">
        <svg class="contact-icon" viewBox="0 0 20 20" aria-hidden="true">
          <circle cx="10" cy="10" r="10" fill="#9e1b24"/>
          <circle cx="10" cy="10" r="5" fill="none" stroke="#fff" stroke-width="1.3"/>
          <path d="M5 10h10M10 5c-2 2.8-2 7.2 0 10M10 5c2 2.8 2 7.2 0 10" fill="none" stroke="#fff" stroke-width="1.1"/>
        </svg>
        <span>www.websitename.com</span>
      </li>
    </ul>

    <address class="address">
      Your Address, City<br>State, Zip 0000
    </address>
  </section>

  <section class="card card-back">
    <div class="back-pattern" role="img" aria-label="Repeating embossed grey brand-mark pattern on dark card stock"></div>
    <div class="back-brand">
      <span class="back-brand-dot" aria-hidden="true"></span>
      <p class="back-brand-name">Harlow Millworks LLC.</p>
    </div>
  </section>
</main>
</body>
</html>
```